WordPress Design for both website and landing page for an expert

I need a clean and stylish design for my new website. I work as an expert (see attached file WHY HOW WHAT), my product is expert opinion (reports) for company evaluations You can use all of the attached pictures colored or black / white. The person is me, you can add other pictures, if you want. The design should be clean and stylish, so you could use white, black, gray, silver and / or one additional color. I have added an idea about my website, see attached file CONCEPT WEBSITE If you have any more information, please do not hesitate to contact us 'Hesitate to ask me ...

```html
<!DOCTYPE html>
<html lang="de">
<head>
<meta charset="utf-8">
<title>Lukas Berndt – Sachverständiger für Firmenbewertungen</title>
<link rel="stylesheet" href="https://fonts.googleapis.com/css2?family=Exo+2:wght@500;600;700&family=Jost:wght@400;500;600&family=Lato:wght@400;700&display=swap">
<style>
:root{
  --ink:#1f1f1f;
  --grey-text:#666a6d;
  --heading-grey:#5c5f62;
  --icon-grey:#aeb7bd;
  --icon-dark:#4a4c4e;
  --navy-text:#2b3a55;
  --pill-bg:#efefef;
  --pill-border:#d9d9d9;
  --footer-bg:#3b3c3d;
  --white:#ffffff;
}
*{margin:0;padding:0;box-sizing:border-box}
html,body{width:1200px;height:2324px;overflow:hidden;background:var(--white)}
body{position:relative;font-family:'Lato',sans-serif;color:var(--ink)}

/* Hero */
.hero{position:absolute;left:0;top:0;width:1200px;height:675px;
  background:linear-gradient(160deg,#5b5e63 0%,#8c9298 35%,#b9bec3 60%,#7d848b 100%)}
.hero-photo{position:absolute;inset:0}
.brand{position:absolute;left:117px;top:92px;width:220px;text-align:center;
  font-family:'Jost',sans-serif;font-weight:400;font-size:21px;letter-spacing:4px;color:var(--white)}
.main-nav{position:absolute;top:64px;left:516px;display:flex;gap:33px;
  font-family:'Jost',sans-serif;font-size:14px;color:var(--white);letter-spacing:.3px}
.main-nav span{position:relative}
.main-nav .active{font-weight:600}
.main-nav .active::after{content:"";position:absolute;left:0;top:22px;width:22px;height:3px;background:var(--white)}
.hero-caption{position:absolute;left:0;top:557px;width:1200px;height:118px;
  background:rgba(70,72,75,.55);text-align:center;color:var(--white)}
.hero-caption h1{font-family:'Exo 2',sans-serif;font-weight:600;font-size:35px;margin-top:18px;letter-spacing:.3px}
.hero-caption p{font-family:'Jost',sans-serif;font-size:19px;margin-top:6px;letter-spacing:.3px}

/* Reasons */
.reasons-mark{position:absolute;top:756px;left:0;width:1200px;text-align:center;
  font-family:'Jost',sans-serif;font-size:22px;letter-spacing:4px;color:#dcdcdc}
.reasons-title{position:absolute;top:814px;left:0;width:1200px;text-align:center;
  font-family:'Exo 2',sans-serif;font-weight:700;font-size:33px;letter-spacing:1px;color:var(--heading-grey)}
.reason{position:absolute;top:920px;width:300px;text-align:center}
.reason svg{display:block;margin:0 auto}
.reason h3{font-family:'Exo 2',sans-serif;font-weight:600;font-size:28px;color:var(--heading-grey);margin-top:38px}
.reason p{font-size:13.5px;line-height:22px;color:var(--ink);margin-top:12px}

/* Promise */
.promise{position:absolute;left:0;top:1297px;width:1200px;height:488px;
  background:linear-gradient(90deg,#d6d5d1 0%,#cfceca 45%,#d8cfc6 70%,#c9a896 100%)}
.promise-mark{position:absolute;left:120px;top:120px;width:440px;text-align:center;
  font-family:'Jost',sans-serif;font-size:44px;letter-spacing:6px;color:rgba(150,150,150,.45)}
.promise h2{position:absolute;left:100px;top:244px;width:485px;text-align:center;
  font-family:'Exo 2',sans-serif;font-weight:700;font-size:34px;color:var(--ink)}
.promise p{position:absolute;left:100px;top:300px;width:485px;text-align:center;
  font-size:22.5px;line-height:40.5px;color:var(--ink)}
.promise-photo{position:absolute;left:610px;top:0;width:590px;height:488px;
  background:linear-gradient(90deg,rgba(214,212,208,0) 0%,rgba(230,225,220,.6) 40%,rgba(196,150,125,.5) 100%)}

/* Questions */
.questions{position:absolute;top:1852px;left:0;width:1200px}
.q-col{position:absolute;list-style:none}
.q-col li{position:relative;padding-left:37px;font-size:14.5px;line-height:21px;color:var(--navy-text);margin-bottom:22px}
.q-col li::before{content:"";position:absolute;left:2px;top:5px;width:11px;height:11px;border-radius:50%;background:#cfd4d8}
.q-left{left:121px;width:450px}
.q-right{left:660px;width:420px}
.q-divider{position:absolute;left:599px;top:6px;width:1px;height:152px;background:#c9c9c9}

/* Call to action */
.cta{position:absolute;left:126px;top:2075px;width:946px;height:76px;border-radius:38px;
  background:var(--pill-bg);border:1px solid var(--pill-border);
  display:flex;align-items:center;justify-content:center;text-align:center;
  font-size:18.5px;line-height:27px;color:var(--grey-text)}
.note{position:absolute;left:150px;top:2168px;width:900px;text-align:center;
  font-size:14.5px;line-height:24px;color:var(--grey-text)}
.note strong{color:var(--ink);font-weight:700}

/* Footer */
.site-footer{position:absolute;left:0;top:2287px;width:1200px;height:37px;background:var(--footer-bg);
  color:var(--white);font-family:'Jost',sans-serif;font-size:13px;text-align:center;line-height:37px}
</style>
</head>
<body>

<header class="hero">
  <div class="hero-photo" role="img" aria-label="Hands writing on a clipboard at a desk with laptop, overlaid with light business charts and diagrams"></div>
  <div class="brand">LUKAS BERNDT</div>
  <nav class="main-nav">
    <span class="active">HOME</span>
    <span>WHAT I DO</span>
    <span>WHY I DO IT &amp; HOW I DO IT</span>
    <span>ABOUT ME</span>
    <span>CONTACT</span>
  </nav>
  <div class="hero-caption">
    <h1>Sachverständiger für Firmenbewertungen</h1>
    <p>Sie benötigen ein Gutachten zur Ermittlung des Wertes Ihres Unternehmens</p>
  </div>
</header>

<section class="reasons">
  <div class="reasons-mark">LUKAS BERNDT</div>
  <h2 class="reasons-title">WHY YOU SHOULD WORK WITH ME</h2>

  <div class="reason" style="left:104px">
    <svg width="270" height="138" viewBox="0 0 270 138">
      <rect x="14" y="12" width="242" height="114" rx="57" fill="none" stroke="var(--icon-grey)" stroke-width="24"/>
      <g stroke="var(--icon-dark)" stroke-width="3" stroke-linecap="round" fill="none">
        <line x1="92" y1="58" x2="122" y2="58"/>
        <line x1="92" y1="69" x2="128" y2="69"/>
        <line x1="92" y1="80" x2="122" y2="80"/>
        <path d="M140 69 H176 M164 57 L178 69 L164 81" stroke-width="5"/>
      </g>
    </svg>
    <h3>Schnell</h3>
    <p>Sie bekommen Ihr Gutachten zeitnah<br>(innerhalb von max. 21 Tagen nach Zugang<br>aller benötigten Unterlagen)</p>
  </div>

  <div class="reason" style="left:450px">
    <svg width="270" height="138" viewBox="0 0 270 138">
      <rect x="14" y="12" width="242" height="114" rx="57" fill="none" stroke="var(--icon-grey)" stroke-width="24"/>
      <g stroke="var(--icon-dark)" stroke-width="3" fill="none">
        <rect x="98" y="40" width="74" height="52" rx="3"/>
        <rect x="104" y="46" width="62" height="40" rx="2" stroke-width="1.5"/>
        <line x1="114" y1="58" x2="156" y2="58"/>
        <line x1="114" y1="66" x2="150" y2="66"/>
        <circle cx="158" cy="88" r="7" fill="var(--white)"/>
        <path d="M154 95 L154 104 L158 100 L162 104 L162 95"/>
      </g>
    </svg>
    <h3>Zertifiziert</h3>
    <p>Sie erhalten ein qualifiziertes und<br>belastbares Gutachten von einem<br>zertifizierten Sachverständigen (höchste<br>Akzeptanz bei allen Parteien)</p>
  </div>

  <div class="reason" style="left:796px">
    <svg width="270" height="138" viewBox="0 0 270 138">
      <rect x="14" y="12" width="242" height="114" rx="57" fill="none" stroke="var(--icon-grey)" stroke-width="24"/>
      <g fill="var(--icon-dark)">
        <rect x="104" y="66" width="66" height="4" rx="2"/>
        <circle cx="114" cy="56" r="10"/>
        <circle cx="160" cy="52" r="14"/>
        <path d="M122 104 L132 76 H142 L152 104 Z"/>
      </g>
    </svg>
    <h3>Verständlich</h3>
    <p>Ihr Gutachten wird für Sie logisch<br>und nachvollziehbar sein und kein<br>“Fachchinesisch” enthalten</p>
  </div>
</section>

<section class="promise">
  <div class="promise-photo" role="img" aria-label="Portrait of the expert in a white shirt leaning on a railing in a bright office"></div>
  <div class="promise-mark">LUKAS BERNDT</div>
  <h2>MY QUALITY PROMISE :</h2>
  <p>should the advised date for the preparation<br>of the report be exceeded, you will receive<br>the report free of chare (I waive my fee)</p>
</section>

<section class="questions">
  <ul class="q-col q-left">
    <li>What are the buying motives of the customers?</li>
    <li>Sie wollen Anteile Ihres Unternehmens oder ihr gesamtes Unternehmen verkaufen?</li>
    <li>Sie müssen im Rahmen einer Trennung/Scheidung jemanden ausbezahlen und benötigen eine Bemessungsgrundlage?</li>
  </ul>
  <div class="q-divider"></div>
  <ul class="q-col q-right">
    <li>Was sind die Kaufmotive der Kunden?</li>
    <li>Sie wollen Ihr Unternehmen auf Ihre Erben übertragen und benötigen eine Bewertung für das Finanzamt?</li>
  </ul>
</section>

<div class="cta">Lassen Sie Ihr Unternehmen von einem qualifizerten Sachverständigen bewerten und gehen somit<br>vielen (unnötigen) Streitereien aus dem Weg.</div>
<p class="note"><strong>Merke</strong>: Die Kosten für ein Gutachten sind immer überproportional günstiger als die Kosten für Rechtsstreitigkeiten. Und das losgelöst von der psychischen Belastung einer solchen Auseinandersetzung ...</p>

<footer class="site-footer">© 2019 by Lukas Berndt. All right reserved.</footer>

</body>
</html>
```